Keystone Disability - Social Security Disability Attorneys

Our company is expanding to attract clients nationwide for our social security disability practice. We have a logo, but I am looking for a creative and elegant letterhead that projects an image of being technologically advanced but still professional enough for the legal field. I am looking for the "wow factor" combined with this is still professional enough for a law practice.

Requesting letterhead and business card design
Updates

Had to update and change the logo. The previous logo had a typo. Please send updates with the new logo for consideration. The letterhead and business cards should be professional enough to be used for a law firm. Thanks.

Industry/Entity Type

Law Practice, Law Firm, Healthcare Industry, Government

Colors

Designer to choose colors to be used in the design.

Requirements
Nice to have
• **Please create a vertical design for the business card**

```html
<!DOCTYPE html>
<html lang="en">
<head>
<meta charset="utf-8">
<title>Keystone Disability – Business Card</title>
<link href="https://fonts.googleapis.com/css2?family=Arimo:wght@400;700&display=swap" rel="stylesheet">
<style>
  :root {
    --backdrop: #e4e4e2;
    --card-white: #ffffff;
    --card-dark: #2e2e2e;
    --card-dark-light: #4a4a4a;
    --accent-orange: #f07f1c;
    --brand-blue: #2d66c6;
    --text-grey: #454545;
    --rule-grey: #8a8a8a;
  }
  * { margin: 0; padding: 0; box-sizing: border-box; }
  html, body { width: 1200px; height: 801px; overflow: hidden; }
  body {
    background: var(--backdrop);
    font-family: "Arimo", Arial, sans-serif;
    position: relative;
  }
  .card {
    position: absolute;
    top: 250px;
    width: 520px;
    height: 300px;
    box-shadow: 0 6px 18px rgba(0,0,0,0.18);
    overflow: hidden;
  }
  .card-front { left: 60px; background: var(--card-white); }
  .card-back { left: 620px; background: var(--card-dark); }

  .brand {
    position: absolute;
    display: flex;
    align-items: center;
    gap: 7px;
    color: var(--brand-blue);
    font-weight: 700;
    letter-spacing: 0.3px;
    text-transform: uppercase;
    white-space: nowrap;
  }
  .brand-dot {
    width: 10px; height: 10px; border-radius: 50%;
    background: var(--brand-blue);
    flex: none;
  }
  .card-front .brand {
    left: 0; width: 290px; top: 140px;
    justify-content: center;
    font-size: 15px;
  }

  .divider {
    position: absolute;
    left: 300px; top: 58px;
    width: 1px; height: 184px;
    background: var(--rule-grey);
  }
  .contact {
    position: absolute;
    left: 318px; top: 58px;
    color: var(--text-grey);
    font-size: 12.5px;
    line-height: 1.35;
  }
  .contact-name {
    color: var(--accent-orange);
    font-weight: 700;
    font-size: 17px;
    letter-spacing: 0.3px;
    text-transform: uppercase;
  }
  .contact-role { margin-bottom: 14px; }
  .contact-address { margin-bottom: 14px; }
  .contact-line { display: flex; align-items: center; gap: 7px; }
  .contact-line svg { width: 11px; height: 11px; flex: none; }

  .pattern {
    position: absolute; inset: 0;
    background: linear-gradient(120deg, var(--card-dark) 0%, #333 45%, var(--card-dark-light) 100%);
  }
  .card-back .brand {
    left: 50%; top: 50%;
    transform: translate(-50%, -50%);
    font-size: 22px;
  }
</style>
</head>
<body>
  <section class="card card-front">
    <div class="brand"><span class="brand-dot"></span>Keystone Disability</div>
    <div class="divider"></div>
    <div class="contact">
      <p class="contact-name">Daniel Carter</p>
      <p class="contact-role">Manager</p>
      <p class="contact-address">Your address, city<br>state, ZIP 0000</p>
      <p class="contact-line">
        <svg viewBox="0 0 12 12"><path d="M3 1 L5 3.5 L4 5 Q5 7.5 7 8 L8.5 7 L11 9 L9.5 11 Q3 10.5 1 2.5 Z" fill="var(--accent-orange)"/></svg>
        555-014-2100
      </p>
      <p class="contact-line">
        <svg viewBox="0 0 12 12"><rect x="1" y="2.5" width="10" height="7" fill="none" stroke="var(--accent-orange)" stroke-width="1.2"/><path d="M1 2.5 L6 6.5 L11 2.5" fill="none" stroke="var(--accent-orange)" stroke-width="1.2"/></svg>
        hello@keystonedisability.com
      </p>
      <p class="contact-line">
        <svg viewBox="0 0 12 12"><circle cx="6" cy="6" r="5" fill="var(--accent-orange)"/><path d="M1 6 H11 M6 1 V11 M2 3.5 H10 M2 8.5 H10" stroke="#fff" stroke-width="0.7"/></svg>
        www.keystonedisability.com
      </p>
    </div>
  </section>

  <section class="card card-back">
    <div class="pattern" role="img" aria-label="Embossed repeating brand-mark pattern across the dark card back"></div>
    <div class="brand"><span class="brand-dot"></span>Keystone Disability</div>
  </section>
</body>
</html>
```